New Brand - Website Design (4 Pages)

We are launching a new brand for electronic cigarettes. We already have logo and packaging done and would like a web design to go with it.

We are interested in the following deliverables:

1) Home Page Design
2) Check Out Design
3) How it Works Page
4) Secondary Template Page Design

Looking for a 60s modern look and something that is consistent with our logo and packaging.

Industry/Entity Type

Electronic

Requirements
Must have
• Consistent with logo and packaging (Use Logo Attached)
White background

Example (Functionality & Design): http://www.torvex.co.uk/
Example (Design): http://www.quillharbor.com/

We want the design more like quillharbor but the functionality the same as torvex.

Top Bar: Pebble Arcs Kits; Cartridge Refills; How it Works; Contact; My Account; Checkout
Should not have
• Stock List or Search Bar or Newsletter Signup

```html
<!DOCTYPE html>
<html lang="en">
<head>
<meta charset="utf-8">
<title>Pebble Arcs – How it Works</title>
<link rel="stylesheet" href="https://fonts.googleapis.com/css2?family=Josefin+Sans:wght@400;600&family=Poiret+One&family=Questrial&display=swap">
<style>
  :root {
    --backdrop: #e6e6e6;
    --backdrop-stripe: #dedede;
    --panel: #ffffff;
    --ink: #1a1a1a;
    --muted: #a9a9a9;
    --rule: #7a7a7a;
    --band-dark: #000000;
    --sky: #8fd6f4;
    --icon-tone: #1d3f4e;
    --on-dark: #ffffff;
  }
  html, body {
    margin: 0;
    padding: 0;
    width: 1127px;
    height: 1200px;
    overflow: hidden;
  }
  body {
    position: relative;
    background: repeating-linear-gradient(90deg, var(--backdrop) 0 3px, var(--backdrop-stripe) 3px 5px);
    font-family: "Questrial", sans-serif;
    color: var(--ink);
  }
  .page {
    position: absolute;
    left: 67px;
    top: 36px;
    width: 984px;
    height: 1094px;
    background: var(--panel);
    box-shadow: 0 2px 6px rgba(0,0,0,0.35);
  }
  .masthead {
    position: absolute;
    left: 0;
    top: 0;
    width: 984px;
    height: 198px;
    background: linear-gradient(180deg, #ffffff 0%, #f4f4f4 70%, #e9e9e9 100%);
  }
  .brand {
    position: absolute;
    left: 0;
    top: 50px;
    width: 984px;
    display: flex;
    align-items: center;
    justify-content: center;
    gap: 22px;
  }
  .brand-dot {
    width: 100px;
    height: 100px;
    border-radius: 50%;
    background: var(--sky);
  }
  .brand-name {
    font-family: "Josefin Sans", sans-serif;
    font-weight: 600;
    font-size: 56px;
    letter-spacing: 3px;
    color: var(--ink);
    margin: 12px 0 0;
  }
  .main-nav {
    position: absolute;
    left: 0;
    top: 244px;
    width: 1127px;
    height: 43px;
    background: var(--panel);
    border: 1px solid #bdbdbd;
    box-sizing: border-box;
    box-shadow: 0 2px 4px rgba(0,0,0,0.25);
    display: flex;
    align-items: center;
    justify-content: center;
    font-size: 18px;
    letter-spacing: 1.2px;
    z-index: 2;
  }
  .main-nav a { color: var(--ink); text-decoration: none; }
  .main-nav .sep { margin: 0 8px; }
  .page-title {
    position: absolute;
    right: 50px;
    top: 286px;
    margin: 0;
    font-family: "Poiret One", sans-serif;
    font-weight: 400;
    font-size: 35px;
    color: var(--muted);
    letter-spacing: 1px;
  }
  .steps {
    position: absolute;
    left: 0;
    top: 373px;
    width: 984px;
    height: 56px;
  }
  .intro {
    position: absolute;
    left: 114px;
    top: 486px;
    width: 756px;
    margin: 0;
    text-align: center;
    font-size: 15.5px;
    line-height: 20px;
    color: var(--ink);
  }
  .flavors {
    position: absolute;
    left: 0;
    top: 634px;
    width: 984px;
    height: 296px;
    background: var(--band-dark);
    color: var(--on-dark);
  }
  .flavors-heading {
    position: absolute;
    left: 0;
    top: 58px;
    width: 984px;
    margin: 0;
    text-align: center;
    font-family: "Josefin Sans", sans-serif;
    font-weight: 400;
    font-size: 29px;
    letter-spacing: 5px;
  }
  .flavors-rule {
    position: absolute;
    top: 75px;
    height: 1px;
    background: var(--rule);
  }
  .flavors-rule.left { left: 17px; width: 370px; }
  .flavors-rule.right { left: 597px; width: 368px; }
  .flavor {
    position: absolute;
    top: 146px;
    width: 170px;
    margin-left: -85px;
    text-align: center;
  }
  .flavor-icon {
    width: 66px;
    height: 66px;
    margin: 0 auto 20px;
    background: var(--icon-tone);
    border-radius: 8px;
  }
  .flavor-name {
    font-size: 17px;
    letter-spacing: 1.6px;
  }
  .flavor-dot {
    position: absolute;
    top: 233px;
    width: 15px;
    height: 15px;
    margin-left: -7px;
    border-radius: 50%;
    background: var(--on-dark);
  }
  .buy-band {
    position: absolute;
    left: 0;
    top: 930px;
    width: 984px;
    height: 120px;
    background: var(--sky);
    display: flex;
    align-items: center;
    justify-content: center;
  }
  .buy-band a {
    font-family: "Josefin Sans", sans-serif;
    font-weight: 600;
    font-size: 29px;
    letter-spacing: 4px;
    color: var(--ink);
    text-decoration: none;
  }
  .site-footer {
    position: absolute;
    left: 0;
    top: 1163px;
    width: 1127px;
    text-align: center;
    font-size: 13px;
    color: #333;
  }
</style>
</head>
<body>
  <div class="page">
    <header class="masthead">
      <div class="brand">
        <div class="brand-dot"></div>
        <p class="brand-name">PEBBLE ARCS</p>
      </div>
    </header>

    <h1 class="page-title">HOW IT WORKS</h1>

    <svg class="steps" viewBox="0 0 984 56" aria-label="Steps 1 to 5">
      <g fill="var(--muted)">
        <circle cx="297" cy="28" r="28"/>
        <circle cx="390" cy="28" r="28"/>
        <circle cx="486" cy="28" r="28"/>
        <circle cx="580" cy="28" r="28"/>
        <circle cx="677" cy="28" r="28"/>
        <circle cx="333" cy="28" r="3"/><circle cx="343" cy="28" r="3"/><circle cx="353" cy="28" r="3"/>
        <circle cx="428" cy="28" r="3"/><circle cx="438" cy="28" r="3"/><circle cx="448" cy="28" r="3"/>
        <circle cx="523" cy="28" r="3"/><circle cx="533" cy="28" r="3"/><circle cx="543" cy="28" r="3"/>
        <circle cx="618" cy="28" r="3"/><circle cx="628" cy="28" r="3"/><circle cx="638" cy="28" r="3"/>
      </g>
      <g fill="#ffffff" font-family="Questrial, sans-serif" font-size="36" text-anchor="middle">
        <text x="297" y="41">1</text>
        <text x="390" y="41">2</text>
        <text x="486" y="41">3</text>
        <text x="580" y="41">4</text>
        <text x="677" y="41">5</text>
      </g>
    </svg>

    <p class="intro">Lorem ipsum dolor sit amet, consectetuer adipiscing elit, sed diam nonummy nibh euismod tincidunt ut laoreet dolore magna aliquam erat volutpat. Ut wisi enim ad minim veniam, quis nostrud exerci tation ullamcorper suscipit lobortis nisl ut aliquip ex ea commodo consequat. Duis autem vel eum iriure dolor in hendrerit in vulputate velit esse molestie consequat,</p>

    <section class="flavors">
      <div class="flavors-rule left"></div>
      <h2 class="flavors-heading">FLAVORS</h2>
      <div class="flavors-rule right"></div>

      <div class="flavor" style="left:139px"><div class="flavor-icon" role="img" aria-label="Tobacco leaf line icon"></div><div class="flavor-name">Tobacco Classic</div></div>
      <div class="flavor" style="left:327px"><div class="flavor-icon" role="img" aria-label="Mint leaves line icon"></div><div class="flavor-name">Menthol</div></div>
      <div class="flavor" style="left:507px"><div class="flavor-icon" role="img" aria-label="Banana line icon"></div><div class="flavor-name">Banana</div></div>
      <div class="flavor" style="left:679px"><div class="flavor-icon" role="img" aria-label="Apple line icon"></div><div class="flavor-name">Apple</div></div>
      <div class="flavor" style="left:855px"><div class="flavor-icon" role="img" aria-label="Thumbs-up in circle line icon"></div><div class="flavor-name">Non-Nicotine</div></div>

      <span class="flavor-dot" style="left:252px"></span>
      <span class="flavor-dot" style="left:405px"></span>
      <span class="flavor-dot" style="left:582px"></span>
      <span class="flavor-dot" style="left:759px"></span>
    </section>

    <div class="buy-band"><a href="#">BUY NOW</a></div>
  </div>

  <nav class="main-nav">
    <a href="#">Home</a><span class="sep">|</span>
    <a href="#">Pebble Arcs Kits</a><span class="sep">|</span>
    <a href="#">Cartridge Refills</a><span class="sep">|</span>
    <a href="#">How it Works</a><span class="sep">|</span>
    <a href="#">Contact</a><span class="sep">|</span>
    <a href="#">My Account</a><span class="sep">|</span>
    <a href="#">Checkout</a>
  </nav>

  <footer class="site-footer">Copyright 2013 PebbleArcs - Terms &amp; Conditions | Privacy Policy</footer>
</body>
</html>
```